Copper Ridge Business Cards For New Startup

I am looking for you to design some business cards for a new startup https://copperridgehub.example. I have supplied logo, brand guidelines and our signatures as a guide.

We need this to reflect the brand guidelines and the website for brand consistency,

What is Copper Ridge?

The Island's Founder Growth Network
Join your new business community full of passionate entrepreneurs who
love to solve problems and help each other grow together!

Any questions you can ask.

Target Market(s)

Business to Business

Contact Information for Business Card

These are attached (signatures) to the job

Font styles to use
Other font styles liked:
• Open Sans

Requirements
Must have
• Match design guidelines
Nice to have
• Photos of our faces so people remember us

```html
<!DOCTYPE html>
<html lang="en">
<head>
<meta charset="utf-8">
<title>Copper Ridge Business Cards</title>
<link href="https://fonts.googleapis.com/css2?family=Open+Sans:wght@400;600;700&display=swap" rel="stylesheet">
<style>
  :root {
    --brand-olive: #5d5b0b;
    --brand-olive-dark: #4a4808;
    --card-white: #ffffff;
    --ink: #1d1d1b;
    --backdrop: #e9eae6;
    --photo-top: #c9cfc4;
    --photo-bottom: #3b4a66;
  }
  * { box-sizing: border-box; margin: 0; padding: 0; }
  html, body {
    width: 1200px; height: 791px; overflow: hidden;
    background: var(--backdrop);
    font-family: "Open Sans", Arial, sans-serif;
  }
  .canvas {
    position: relative; width: 1200px; height: 791px;
  }
  .card {
    position: absolute; top: 235px;
    width: 520px; height: 320px;
    border-radius: 18px;
    box-shadow: 0 10px 30px rgba(0,0,0,0.12);
    overflow: hidden;
  }
  /* Front */
  .card--front {
    left: 60px;
    background: var(--brand-olive);
    display: flex; flex-direction: column; align-items: center; justify-content: center;
    gap: 22px;
  }
  .front-mark {
    width: 96px; height: 96px; border-radius: 50%;
    border: 3px solid var(--card-white);
  }
  .front-name {
    color: var(--card-white);
    font-weight: 600; font-size: 26px; letter-spacing: 0.5px;
    text-transform: uppercase;
  }
  /* Back */
  .card--back {
    left: 620px;
    background: var(--card-white);
  }
  .brand-lockup {
    position: absolute; left: 30px; top: 62px;
    display: flex; align-items: center; gap: 14px;
  }
  .brand-mark {
    width: 52px; height: 52px; border-radius: 50%;
    border: 2.5px solid var(--brand-olive);
  }
  .brand-name {
    color: var(--brand-olive);
    font-weight: 700; font-size: 27px; line-height: 1;
    text-transform: uppercase;
  }
  .brand-tagline {
    color: var(--brand-olive);
    font-weight: 600; font-size: 10px; margin-top: 5px;
  }
  .portrait {
    position: absolute; right: 36px; top: 26px;
    width: 108px; height: 108px;
    background: linear-gradient(180deg, var(--photo-top), var(--photo-bottom));
  }
  .person {
    position: absolute; left: 30px; bottom: 48px;
  }
  .person-name {
    color: var(--brand-olive);
    font-weight: 700; font-size: 22px; line-height: 1.1;
  }
  .person-role {
    color: var(--ink);
    font-weight: 600; font-size: 12px;
  }
  .contact {
    position: absolute; right: 30px; bottom: 40px;
    border-left: 2px solid var(--brand-olive);
    padding-left: 16px;
    display: grid; grid-template-columns: auto auto; column-gap: 10px; row-gap: 4px;
    font-size: 11.5px; color: var(--ink);
  }
  .contact dt { color: var(--brand-olive); font-weight: 600; }
  .contact dd { font-weight: 600; }
</style>
</head>
<body>
<main class="canvas">
  <section class="card card--front" aria-label="Card front">
    <div class="front-mark"></div>
    <p class="front-name">Copper Ridge</p>
  </section>

  <section class="card card--back" aria-label="Card back">
    <div class="brand-lockup">
      <div class="brand-mark"></div>
      <div>
        <p class="brand-name">Copper Ridge</p>
        <p class="brand-tagline">The Island's Founder Growth Network</p>
      </div>
    </div>
    <div class="portrait" role="img" aria-label="Portrait photo of the card holder"></div>
    <div class="person">
      <p class="person-name">Daniel Moreno</p>
      <p class="person-role">Founder &amp; Growth Hacker</p>
    </div>
    <dl class="contact">
      <dt>M:</dt><dd>+34 611 204 377</dd>
      <dt>E:</dt><dd>dm@copperridgehub.example</dd>
      <dt>W:</dt><dd>www.copperridgehub.example</dd>
    </dl>
  </section>
</main>
</body>
</html>
```